Design the packaging for a wholesale/retail Date fruit company

We need a box designed for a dates fruit box. This will be used for the wholesale packaging. The brand is called Nur Safa Dates , it is a new business. Nur Safa means the home. It will be part of a food exporting business called Nur Safa Foods. It will be based out of the Middle East and the Holy Lands. Recently Qatar had a grand games and one of their stadiums was also called Nur Safa, it was designed to represent an Arabian tent. The logo hasn't been designed yet but something simple is fine. I also have a sample design, you can use most of the information from. The product is a Product of Palestine, it is in 5kg boxes the nutritional information is on the sample.

The company is called Haris Nadeem General Trading (Haris Nadeem General Trading) based in Doha Qatar. Logo is provided.

The exporter details are on the sample box.
Use this companies packaging as inspiration for what we are looking to compete with https://marovine.com/

I require the illustrator/photoshop files please so that we can update details on it.

Industry/Entity Type

food (dates)

Requirements
Must have
• English & Arabic text
Nice to have
• try and incorporate the colour CFB53B

```html
<!DOCTYPE html>
<html lang="en">
<head>
<meta charset="utf-8">
<title>Nur Safa Dates – Medjool 5kg Box Dieline</title>
<link href="https://fonts.googleapis.com/css2?family=Aref+Ruqaa:wght@700&family=Great+Vibes&family=Hind:wght@400;600&family=Hind+Siliguri:wght@400;600&family=Lalezar&family=Libre+Baskerville&family=Cairo:wght@400;700&display=swap" rel="stylesheet">
<style>
:root{
  --sheet:#231f20;
  --stage:#f5f7d8;
  --straw:#e3d272;
  --panel:#2a292a;
  --red:#b5262e;
  --green:#55a04b;
  --badge-green:#4e9656;
  --gold:#dcc76c;
  --gold-deep:#cfb53b;
  --ink:#1e1c1c;
  --brown:#7a6a3e;
  --cream:#f4efe0;
  --cut:#ffffff;
}
*{box-sizing:border-box;margin:0;padding:0}
html,body{width:795px;height:1200px;overflow:hidden}
body{background:var(--stage);position:relative;font-family:'Libre Baskerville',serif}
.sheet{position:absolute;left:0;top:0;width:795px;height:659px;background:var(--sheet)}
.abs{position:absolute}
.cut-margin{position:absolute;left:121px;top:0;width:553px;height:659px;background:var(--cut)}
.flap{position:absolute;background:var(--straw)}
.flap--red{background:var(--red)}
.flap svg{position:absolute;inset:0}
.lid{position:absolute;left:124px;top:0;width:547px;height:123px;background:var(--straw)}
.front{position:absolute;left:124px;top:123px;width:547px;height:413px;background:var(--straw)}
.side{position:absolute;top:123px;width:118px;height:413px;background:var(--straw)}
.side--left{left:6px}
.side--right{left:671px}
.base{position:absolute;left:124px;top:536px;width:544px;height:118px;background:var(--red)}
.dark-field{position:absolute;left:158px;top:6px;width:479px;height:395px;background:var(--panel)}
.photo{position:absolute;border-radius:45% 50% 40% 48%;background:radial-gradient(ellipse at 45% 40%,#9b2a22 0%,#6e1a14 55%,#3d0d0a 100%)}
.ornament{position:absolute;background:linear-gradient(90deg,rgba(207,181,59,.75),rgba(207,181,59,.45))}
.seal{position:absolute;border-radius:50%;background:radial-gradient(circle,#d8b552 0%,#b08a2a 100%);border:2px solid #c9a440}
.t{position:absolute;white-space:nowrap;line-height:1}
.c{text-align:center}
.brand-ar{font-family:'Aref Ruqaa',serif;color:var(--gold);font-weight:700}
.brand-en{font-family:'Libre Baskerville',serif}
.kufi{font-family:'Lalezar',system-ui,sans-serif}
.serif{font-family:'Libre Baskerville',serif}
.script{font-family:'Great Vibes',cursive}
.hindi{font-family:'Hind',sans-serif}
.bangla{font-family:'Hind Siliguri',sans-serif}
.arabic{font-family:'Cairo',sans-serif}
.rule{position:absolute;height:1px;background:linear-gradient(90deg,transparent,var(--gold),transparent)}
.rule--brown{background:linear-gradient(90deg,transparent,#a0853a,transparent)}
.net-badge{position:absolute;left:189px;top:499px;width:99px;height:37px;background:var(--badge-green);clip-path:polygon(0 18%,50% 0,100% 18%,100% 100%,0 100%)}
.quality-box{position:absolute;left:189px;top:560px;width:99px;height:94px;background:var(--ink)}
.rot{position:absolute;transform-origin:0 0}
.lid-print{position:absolute;left:158px;top:6px;width:479px;height:116px;transform:rotate(180deg);color:var(--cream)}
.nutrition{position:absolute;left:149px;top:4px;width:112px;border:1px solid var(--cream);background:#fff;border-collapse:collapse;font-family:'Cairo',sans-serif;font-size:4.3px;color:var(--ink)}
.nutrition th{background:#5a4a4c;color:#fff;font-weight:400;padding:1px 2px;text-align:left}
.nutrition td{border-top:0.5px solid #555;padding:.6px 2px;line-height:1.15}
.nutrition td.ar{text-align:right}
.date-box{position:absolute;left:293px;top:22px;width:62px;height:29px;background:#fff;border-radius:3px}
.trader-name{font-family:'Libre Baskerville',serif;font-size:11px;color:var(--ink);line-height:1.35}
.trader-mark{position:absolute;width:9px;height:9px;background:var(--ink)}
</style>
</head>
<body>
<main class="sheet" aria-label="Nur Safa Dates 5kg box dieline">

  <div class="cut-margin"></div>

  <!-- corner flaps -->
  <div class="flap" style="left:11px;top:14px;width:111px;height:108px;clip-path:polygon(0 0,70% 0,100% 100%,0 100%)">
    <svg width="111" height="108"><g stroke="#9b8f55" stroke-width=".6"><line x1="15" y1="70" x2="55" y2="30"/><line x1="25" y1="95" x2="75" y2="45"/><line x1="45" y1="98" x2="85" y2="58"/></g></svg>
  </div>
  <div class="flap" style="left:674px;top:14px;width:111px;height:108px;clip-path:polygon(30% 0,100% 0,100% 100%,0 100%)">
    <svg width="111" height="108"><g stroke="#9b8f55" stroke-width=".6"><line x1="35" y1="40" x2="75" y2="80"/><line x1="45" y1="25" x2="95" y2="75"/><line x1="60" y1="20" x2="100" y2="60"/></g></svg>
  </div>
  <div class="flap flap--red" style="left:11px;top:537px;width:111px;height:108px;clip-path:polygon(0 0,100% 0,80% 100%,0 100%)">
    <svg width="111" height="108"><g stroke="#e48a86" stroke-width=".6"><line x1="15" y1="10" x2="60" y2="55"/><line x1="30" y1="8" x2="90" y2="68"/><line x1="15" y1="50" x2="55" y2="90"/></g></svg>
  </div>
  <div class="flap flap--red" style="left:674px;top:537px;width:111px;height:108px;clip-path:polygon(0 0,100% 0,100% 100%,20% 100%)">
    <svg width="111" height="108"><g stroke="#e48a86" stroke-width=".6"><line x1="55" y1="10" x2="15" y2="50"/><line x1="90" y1="12" x2="40" y2="62"/><line x1="95" y1="50" x2="55" y2="90"/></g></svg>
  </div>

  <!-- main panels -->
  <div class="lid"></div>
  <div class="front"></div>
  <div class="side side--left"></div>
  <div class="side side--right"></div>
  <div class="base"></div>

  <div class="dark-field" role="img" aria-label="Dark charcoal field with a faint geometric star pattern"></div>

  <!-- lid print (reads upside-down) -->
  <section class="lid-print" aria-label="Lid information">
    <p class="t arabic" style="left:145px;top:97px;font-size:5px;direction:rtl">تمر مجول طبيعي طازج يحتوي على النوى</p>
    <p class="t serif" style="left:145px;top:104px;font-size:5px">Fresh Natural Medjool Dates which includes Pits</p>
    <table class="nutrition">
      <tr><th>Nutrition Facts<br>Serving Size (100 g)</th><th style="text-align:right">القيمة الغذائية<br>(لكل 100 غ)</th><th></th></tr>
      <tr><td>Energy (KCAL)</td><td>268</td><td class="ar">طاقة</td></tr>
      <tr><td>Carbohydrate (g)</td><td>64</td><td class="ar">كربوهيدرات</td></tr>
      <tr><td>Protein (g)</td><td>2</td><td class="ar">بروتين</td></tr>
      <tr><td>Fat (g)</td><td>0</td><td class="ar">دهون</td></tr>
      <tr><td>Sodium (mg)</td><td>0</td><td class="ar">صوديوم</td></tr>
      <tr><td>Cholesterol (g)</td><td>0</td><td class="ar">كوليسترول</td></tr>
      <tr><td>Dietary Fibers (g)</td><td>6</td><td class="ar">ألياف غذائية</td></tr>
      <tr><td>Iron (mg)</td><td>2</td><td class="ar">حديد</td></tr>
      <tr><td>Magnesium (mg)</td><td>35</td><td class="ar">مغنيسيوم</td></tr>
      <tr><td>Potassium (mg)</td><td>650</td><td class="ar">بوتاسيوم</td></tr>
    </table>
    <p class="t arabic" style="left:279px;top:11px;font-size:5.5px;direction:rtl">تاريخ الإنتاج والانتهاء</p>
    <p class="t serif" style="left:278px;top:30px;font-size:5.5px">Pro:</p>
    <p class="t serif" style="left:278px;top:42px;font-size:5.5px">Exp:</p>
    <div class="date-box"></div>
    <p class="t arabic" style="left:281px;top:61px;font-size:5.5px;direction:rtl">إنتاج فلسطين</p>
    <p class="t serif" style="left:281px;top:70px;font-size:5px">Produce of Palestine</p>
    <div class="abs" style="left:281px;top:80px;width:50px;height:1px;background:var(--cream)"></div>
    <p class="t arabic" style="left:278px;top:86px;font-size:5px;direction:rtl">يحفظ في مكان بارد وجاف</p>
    <p class="t serif" style="left:278px;top:95px;font-size:5px">Store in Cool &amp; Dry Place</p>
    <p class="t brand-ar" style="left:362px;top:14px;font-size:20px;color:var(--green)">نور صفا</p>
    <p class="t brand-en" style="left:372px;top:40px;font-size:8px;color:var(--green)">Nur Safa Dates</p>
  </section>

  <!-- front panel -->
  <p class="t brand-ar c" style="left:193px;top:168px;width:202px;font-size:58px">نور صفا</p>
  <p class="t brand-en c" style="left:190px;top:253px;width:210px;font-size:25px;color:#fff">Nur Safa Dates</p>

  <p class="t kufi c" style="left:444px;top:193px;width:174px;font-size:40px;color:var(--green)">تمر مجول</p>
  <p class="t kufi c" style="left:444px;top:234px;width:174px;font-size:32px;color:#fff">فلسطيني</p>
  <div class="rule" style="left:464px;top:274px;width:130px"></div>
  <p class="t serif c" style="left:444px;top:284px;width:174px;font-size:20px;color:#fff;line-height:1.1">MEDJOOL<br>DATES</p>
  <p class="t script c" style="left:444px;top:331px;width:174px;font-size:27px;color:#fff">Natural Sweetness</p>

  <div class="seal" role="img" aria-label="Round gold quality seal" style="left:499px;top:366px;width:64px;height:66px"></div>

  <div class="photo" role="img" aria-label="Heap of glossy Medjool dates" style="left:182px;top:304px;width:224px;height:168px"></div>

  <p class="t hindi c" style="left:455px;top:443px;width:150px;font-size:18px;font-weight:600;color:var(--ink)">नूर सफ़ा खजूर</p>
  <p class="t hindi c" style="left:455px;top:466px;width:150px;font-size:9.5px;color:var(--brown);font-style:italic">मेड्जूल खजूर प्राकृतिक मिठास</p>
  <div class="rule rule--brown" style="left:464px;top:483px;width:130px"></div>

  <svg class="abs" style="left:467px;top:499px" width="38" height="19" viewBox="0 0 38 19" aria-label="Flag of Palestine" role="img">
    <rect width="38" height="6.33" fill="#1e1c1c"/><rect y="6.33" width="38" height="6.34" fill="#fff"/><rect y="12.67" width="38" height="6.33" fill="#3f9a46"/><polygon points="0,0 14,9.5 0,19" fill="#c8202b"/>
  </svg>
  <p class="t arabic" style="left:507px;top:497px;font-size:8px;color:var(--ink)">إنتاج فلسطين</p>
  <p class="t serif" style="left:507px;top:511px;font-size:9.5px;color:var(--ink)">Produce of Palestine</p>

  <p class="t bangla" style="left:302px;top:492px;font-size:12px;font-weight:600;color:var(--ink)">নূর সাফা খেজুর</p>
  <p class="t bangla" style="left:302px;top:511px;font-size:9.5px;color:var(--ink)">মেডজুল তারিখ প্রাকৃতিক মিষ্টি</p>

  <div class="net-badge"></div>
  <p class="t serif c" style="left:189px;top:515px;width:99px;font-size:8px;color:var(--ink)">Net Wet. 5kg/11 lbs</p>

  <!-- left side panel -->
  <div class="ornament" role="img" aria-label="Column of gold chevron ornaments" style="left:96px;top:210px;width:54px;height:186px;clip-path:polygon(0 0,100% 0,70% 100%,0 100%)"></div>
  <div class="rot" style="left:124px;top:123px;width:413px;height:118px;transform:rotate(90deg)">
    <p class="t brand-ar" style="left:62px;top:18px;font-size:30px;color:var(--ink)">نور صفا</p>
    <p class="t brand-en" style="left:62px;top:57px;font-size:9.5px;color:var(--ink)">Nur Safa Dates</p>
    <p class="t serif" style="left:62px;top:77px;font-size:6.5px;color:var(--ink)">info@nursafadates.com</p>
    <p class="t serif" style="left:62px;top:88px;font-size:6.5px;color:var(--ink)">www.nursafadates.com</p>
    <div class="trader-mark" style="left:168px;top:46px"></div>
    <p class="t trader-name" style="left:183px;top:41px">Haris Nadeem<br>General Trading</p>
    <div class="abs" style="left:272px;top:60px;width:1px;height:22px;background:var(--ink)"></div>
    <p class="t serif" style="left:278px;top:63px;font-size:6.5px;color:var(--ink)">sales@hngtrading.com</p>
    <p class="t serif" style="left:278px;top:74px;font-size:6.5px;color:var(--ink)">www.hngtrading.com</p>
  </div>

  <!-- right side panel -->
  <div class="rot" style="left:671px;top:536px;width:413px;height:118px;transform:rotate(-90deg)">
    <p class="t brand-ar" style="left:204px;top:30px;font-size:38px;color:var(--ink)">نور صفا</p>
    <p class="t brand-en" style="left:204px;top:78px;font-size:16px;color:var(--ink)">Nur Safa Dates</p>
  </div>
  <div class="photo" role="img" aria-label="Cluster of Medjool dates" style="left:690px;top:355px;width:86px;height:124px"></div>

  <!-- base band -->
  <p class="t arabic c" style="left:189px;top:541px;width:99px;font-size:11px;color:var(--ink)">جودة فاخرة طبيعي</p>
  <div class="quality-box"></div>
  <p class="t serif c" style="left:189px;top:568px;width:99px;font-size:8px;color:var(--gold);line-height:1.4">100% Natural<br>Premium Quality</p>

  <p class="t kufi c" style="left:318px;top:549px;width:160px;font-size:34px;color:var(--gold)">تمر مجول</p>
  <div class="rule" style="left:350px;top:590px;width:95px"></div>
  <p class="t serif c" style="left:318px;top:597px;width:160px;font-size:13.5px;color:var(--gold)">MEDJOOL DATES</p>
  <p class="t script c" style="left:318px;top:612px;width:160px;font-size:22px;color:var(--gold)">Natural Sweetness</p>

</main>
</body>
</html>
```